Coffee Promotion for Specialty Coffees

I need to have a poster designed to promote our coffee sales. We offer cappuccino for $3.75, Latte for $3.75, Americano for $2.00, Espresso $2.00 and Fair Trade Organic Colombian Coffee for $1.75 Med, $2.00L Large. I would like sometihng very visual that shows the coffees and also has the pricing, and includes the wording" Try our Amazing Specialty Coffees!" Our logo is attached as well

Poster size is 24" wide x 36" high

Target Market(s)

Seniors and Students in a Mall Setting

Colors

Designer to choose colors to be used in the design.

Requirements
Must have
• Graphic artwork of coffees (cappuccinos, lattes, etc). Logo included in artwork. Must be for 24"wide x 36" high poster
Nice to have
• Would like something that shows closeups of the coffees and visually sells the coffee being premium and delicious.

```html
<!DOCTYPE html>
<html lang="en">
<head>
<meta charset="utf-8">
<title>Swirlbury Coffee Menu Poster</title>
<link href="https://fonts.googleapis.com/css2?family=Sorts+Mill+Goudy&family=Montserrat:wght@700&display=swap" rel="stylesheet">
<style>
  :root {
    --page-bg: #e6e4e1;
    --poster-dark: #0b0b0d;
    --photo-brown: #3a2516;
    --photo-navy: #0f1a2c;
    --cup-blue: #1d3f7a;
    --ink-light: #f4f1ea;
    --accent-gold: #f5a81c;
    --ribbon-ink: #1a1408;
    --badge-fill: #262427;
  }
  * { margin: 0; padding: 0; box-sizing: border-box; }
  html, body { width: 1101px; height: 1200px; overflow: hidden; background: var(--page-bg); }
  .poster {
    position: absolute; left: 170px; top: 30px; width: 760px; height: 1140px;
    background: var(--poster-dark); overflow: hidden;
    font-family: "Sorts Mill Goudy", Georgia, serif; color: var(--ink-light);
  }
  .poster-photo {
    position: absolute; inset: 0;
    background:
      radial-gradient(ellipse 55% 30% at 55% 62%, var(--cup-blue) 0%, var(--photo-navy) 55%, transparent 80%),
      radial-gradient(ellipse 45% 40% at 80% 25%, var(--photo-brown) 0%, transparent 75%),
      radial-gradient(ellipse 40% 35% at 15% 55%, #2b1a0f 0%, transparent 75%),
      linear-gradient(180deg, #120d0a 0%, #1a120c 40%, #0a0b10 100%);
  }
  .brand-badge {
    position: absolute; left: 260px; top: 70px; width: 240px; height: 240px;
    border-radius: 50%; background: var(--badge-fill);
    border: 3px solid #3b393c;
    display: flex; align-items: center; justify-content: center;
  }
  .brand-name { font-size: 44px; color: var(--ink-light); }
  .menu-title {
    position: absolute; top: 340px; width: 100%; text-align: center;
    font-size: 54px; letter-spacing: 0.5px;
  }
  .menu-frame {
    position: absolute; left: 110px; top: 425px; width: 545px; height: 500px;
    border: 2px solid var(--ink-light);
  }
  .promo-ribbon {
    position: absolute; left: 175px; top: 402px; width: 385px; height: 42px;
    background: var(--accent-gold); color: var(--ribbon-ink);
    font-family: "Montserrat", Arial, sans-serif; font-weight: 700; font-size: 16px;
    display: flex; align-items: center; justify-content: center;
    clip-path: polygon(0 0, 100% 0, 97% 50%, 100% 100%, 0 100%, 3% 50%);
  }
  .menu-list { position: absolute; left: 110px; top: 470px; width: 545px; list-style: none; }
  .menu-item {
    text-align: center; font-size: 24px; padding: 16px 0 22px;
    margin: 0 135px; border-bottom: 1.5px dashed rgba(244,241,234,0.85);
    white-space: nowrap;
  }
  .menu-item:nth-child(n+2) { margin-top: 12px; }
  .menu-item.featured { border-bottom: none; margin: 22px 0 0; padding: 0; line-height: 1.2; }
  .price { color: var(--accent-gold); }
</style>
</head>
<body>
  <main class="poster">
    <div class="poster-photo" role="img" aria-label="Close-up photo of a dark coffee cup on a blue saucer with scattered roasted beans and a coffee grinder behind, steam rising"></div>

    <div class="brand-badge"><span class="brand-name">Swirlbury</span></div>

    <h1 class="menu-title">Coffee Menu</h1>

    <div class="menu-frame"></div>
    <div class="promo-ribbon">Try our Amazing Specialty Coffees!</div>

    <ul class="menu-list">
      <li class="menu-item">Cappuccino <span class="price">$3.75</span></li>
      <li class="menu-item">Latte <span class="price">$3.75</span></li>
      <li class="menu-item">Americano <span class="price">$2.00</span></li>
      <li class="menu-item">Espresso <span class="price">$2.00</span></li>
      <li class="menu-item featured">Fair Trade Organic Colombian Coffee<br><span class="price">$1.75 Med, $2.00L Large</span></li>
    </ul>
  </main>
</body>
</html>
```